Clearbrook Systems Design - Van Wrap

I am looking for a new graphic design with our company logo and banner that emphasizes water, coffee, and Ice without showcasing our specific products. I want to let you know that these systems do not include 5-gallon jugs. Please do not add any images of 5-gallon jugs. If possible, I would like images of a splash of water or a banner of ice and coffee beans. This will go on a 2024 Vell 2200 Tarnvan short-body high roof. I look forward to seeing your design!

```html
<!DOCTYPE html>
<html lang="en">
<head>
<meta charset="utf-8">
<title>Holvane Office Solutions – Van Wrap Banner</title>
<link rel="stylesheet" href="https://fonts.googleapis.com/css2?family=Ubuntu:wght@400;500;700&display=swap">
<style>
  :root {
    --stage: #4d4d4d;
    --green-light: #72c15e;
    --green-mid: #59a553;
    --green-brand: #4fb83a;
    --name-green: #5cb82e;
    --swoosh-grey: #c4c4c4;
    --panel-white: #ffffff;
    --text-grey: #7a7a7a;
  }
  html, body {
    margin: 0;
    padding: 0;
    width: 1200px;
    height: 1200px;
    overflow: hidden;
    background: var(--stage);
    font-family: "Ubuntu", sans-serif;
  }
  .canvas {
    position: relative;
    width: 1200px;
    height: 1200px;
    display: flex;
    align-items: center;
    justify-content: center;
  }
  .wrap-banner {
    width: 1100px;
    height: 194px;
    display: block;
  }
  .service-label {
    font-family: "Ubuntu", sans-serif;
    font-weight: 700;
    font-size: 15px;
    fill: var(--green-light);
    letter-spacing: 0.5px;
  }
  .site-address {
    font-family: "Ubuntu", sans-serif;
    font-weight: 500;
    font-size: 50px;
    fill: var(--panel-white);
  }
  .brand-name {
    font-family: "Ubuntu", sans-serif;
    font-weight: 700;
    font-size: 60px;
    fill: var(--name-green);
  }
  .brand-descriptor {
    font-family: "Ubuntu", sans-serif;
    font-weight: 500;
    font-size: 24px;
    fill: var(--text-grey);
  }
  .brand-since {
    font-family: "Ubuntu", sans-serif;
    font-weight: 400;
    font-size: 16px;
    fill: var(--text-grey);
  }
</style>
</head>
<body>
<main class="canvas">
  <svg class="wrap-banner" viewBox="0 0 1309 231" xmlns="http://www.w3.org/2000/svg">
    <defs>
      <clipPath id="banner-shape">
        <rect x="0" y="0" width="1309" height="231" rx="8" ry="8"/>
      </clipPath>
    </defs>

    <g clip-path="url(#banner-shape)">
      <rect class="field-right" x="0" y="0" width="1309" height="231" fill="var(--green-mid)"/>
      <rect class="field-upper" x="0" y="0" width="760" height="148" fill="var(--green-light)"/>
      <path class="swoosh-left" d="M560 0 Q680 40 712 231 L790 231 Q760 60 640 0 Z" fill="var(--swoosh-grey)"/>
      <path class="brand-panel" d="M610 0 Q730 50 760 231 L1230 231 Q1190 50 1090 0 Z" fill="var(--panel-white)"/>
      <path class="swoosh-right" d="M1070 0 Q1180 60 1225 231 L1275 231 Q1240 60 1160 0 Z" fill="var(--swoosh-grey)"/>
      <path class="field-edge" d="M1095 0 Q1215 60 1262 231 L1309 231 L1309 0 Z" fill="var(--green-mid)"/>
    </g>

    <g class="service-tile tile-coffee">
      <rect x="82" y="34" width="141" height="92" rx="9" fill="var(--panel-white)"/>
      <rect x="86" y="38" width="94" height="84" rx="6" fill="var(--green-light)" role="img" aria-label="Coffee cup icon"/>
      <text class="service-label" transform="translate(207 80) rotate(-90)" text-anchor="middle">COFFEE</text>
    </g>
    <g class="service-tile tile-water">
      <rect x="252" y="34" width="141" height="92" rx="9" fill="var(--panel-white)"/>
      <rect x="256" y="38" width="108" height="84" rx="6" fill="var(--green-light)" role="img" aria-label="Water drop and waves icon"/>
      <text class="service-label" transform="translate(378 80) rotate(-90)" text-anchor="middle">WATER</text>
    </g>
    <g class="service-tile tile-ice">
      <rect x="422" y="32" width="147" height="96" rx="9" fill="var(--panel-white)"/>
      <rect x="426" y="36" width="96" height="88" rx="6" fill="var(--green-light)" role="img" aria-label="Ice cubes and snowflake icon"/>
      <text class="service-label" transform="translate(548 100) rotate(-90)" text-anchor="middle">ICE</text>
    </g>

    <text class="site-address" x="80" y="206" textLength="598" lengthAdjust="spacingAndGlyphs">holvaneofficesolutions.com</text>

    <circle class="brand-dot" cx="815" cy="117" r="60" fill="var(--green-brand)"/>
    <text class="brand-name" x="892" y="122" textLength="238" lengthAdjust="spacing">HOLVANE</text>
    <text class="brand-descriptor" x="892" y="157" textLength="238" lengthAdjust="spacing">office solutions</text>
    <text class="brand-since" x="1130" y="184" text-anchor="end">Since 1958</text>
  </svg>
</main>
</body>
</html>
```